Clever Cargo Trike Ad Campaign

I've started a cargo trike company in Washington, DC that will generate revenue from deliveries, promotions and advertising. The trikes have three large ad panel spaces that are perfect for banners. While I'll be using these for promoting customer products/services, I'd like a creative ad that also promotes my own company when not promoting others.

The trikes are human pedal powered, with electric-assist. They can carry 550 lbs and 62 cubic feet of cargo anywhere in DC's downtown area. They make no noise, don't block streets while delivering goods, move around town as quickly as vans or trucks, have zero tailipipe emissions, can use bike lanes, reduce street congestion, etc. In shortly, they are eco-friendly, low-impact, socially-responsible, dependable and efficient!

I'd also like to convey that the trikes are available for advertising and promotional campaigns.....

I'd like a campaign that conveys some of the above, but in a clever, (maybe even humorous) fashion. Not sure if each of three panels (54"x30", 54"x30", 37"x33") needs same ad or just similar ones. Campaign should be geared toward potential customers (organic drycleaners, bakeries, office supply, caterers, farmshare food deliveries, etc), but also be pertinent to anyone who views.

I've included our company logo and a graphic I created that shows the DC skyline (as yet unused). Also included a photo of one of the trikes.

Target Market(s)

* Businesses within Washington, DC that are seeking a unique delivery service.
* Large/small businesses seeking a dedicated, effective ad campaign venue in DC
* Any business seeking to promote products/services (hand out samples or brochures, represent them a street fairs, etc.)

Industry/Entity Type

It Company

Requirements
Must have
• I can easily come up with my own plain, straightforward ad campaign. I'm looking for something creative, unique, attractive that doesn't overwhelm the customer with information. I want it to convey what we have to offer potential customers.
Nice to have
• It would be great it if were humorous, had some kind of Washington focus, etc. But these are not crucial. While I'd like to somehow address the "eco-friendly" aspect of the company, I don't want this to be the sole focus.
• Thus, we can use colors other than the green in my logo, as long as they go well with what I have.
Should not have
• While I'm no fan of today's DC political environment, I don't want a campaign that will bring adverse attention to my company.

```html
<!DOCTYPE html>
<html lang="en">
<head>
<meta charset="utf-8">
<title>Haulway Cargo Trike Panels</title>
<link href="https://fonts.googleapis.com/css2?family=Montserrat:wght@400;700;800;900&family=Quicksand:wght@300;400&family=Open+Sans:wght@600&display=swap" rel="stylesheet">
<style>
  :root {
    --brand-green: #0e8c39;
    --label-green: #13883a;
    --white: #ffffff;
    --stage-light: #f6f6f6;
    --stage-dark: #e2e2e2;
  }
  * { box-sizing: border-box; margin: 0; padding: 0; }
  html, body { width: 1200px; height: 1200px; overflow: hidden; }
  body {
    position: relative;
    background: radial-gradient(circle at 50% 45%, var(--stage-light) 0%, var(--stage-dark) 100%);
    font-family: "Montserrat", sans-serif;
  }
  .size-label {
    position: absolute;
    font-family: "Quicksand", sans-serif;
    font-weight: 300;
    font-size: 47px;
    letter-spacing: 2px;
    color: var(--label-green);
    line-height: 1;
  }
  .panel { position: absolute; background: var(--white); }
  .panel--wide { left: 236px; width: 730px; height: 380px; }
  .panel--square { left: 394px; top: 816px; width: 412px; height: 376px; }

  .band-headline {
    position: absolute; left: 0; right: 0; top: 0;
    background: var(--brand-green); color: var(--white);
    text-align: center;
  }
  .panel--wide .band-headline { height: 135px; }
  .panel--square .band-headline { height: 141px; }

  .headline { font-weight: 800; line-height: 1; }
  .headline--tight { font-size: 34px; letter-spacing: -0.5px; padding-top: 29px; }
  .headline--spaced { font-size: 33px; letter-spacing: 6px; padding-top: 28px; }
  .headline--stacked { font-size: 23px; letter-spacing: 2.4px; line-height: 1.2; padding-top: 33px; }
  .subline {
    font-family: "Quicksand", sans-serif; font-weight: 400;
    line-height: 1; margin-top: 6px;
  }
  .subline--small { font-size: 22px; letter-spacing: 1.6px; }
  .subline--large { font-size: 26px; letter-spacing: 2.6px; }
  .subline--square { font-size: 21px; letter-spacing: 1.6px; margin-top: 8px; }

  .band-brand { position: absolute; left: 0; right: 0; background: var(--white); }
  .panel--wide .band-brand { top: 135px; height: 112px; }
  .panel--square .band-brand { top: 141px; height: 111px; }

  .brand-lockup { position: absolute; display: flex; align-items: center; gap: 16px; }
  .panel--wide .brand-lockup { left: 62px; top: 0; bottom: 0; }
  .panel--square .brand-lockup { left: 80px; top: 0; bottom: 0; }
  .brand-name {
    font-weight: 900; color: var(--brand-green);
    line-height: 1; letter-spacing: 1px;
  }
  .panel--wide .brand-name { font-size: 40px; }
  .panel--square .brand-name { font-size: 32px; }
  .brand-dot { border-radius: 50%; background: var(--brand-green); }
  .panel--wide .brand-dot { width: 40px; height: 40px; }
  .panel--square .brand-dot { width: 32px; height: 32px; }

  .web-address {
    position: absolute; right: 38px; top: 0; line-height: 112px;
    font-family: "Quicksand", sans-serif; font-weight: 400;
    font-size: 31px; letter-spacing: 2px; color: var(--brand-green);
  }

  .band-benefits {
    position: absolute; left: 0; right: 0; top: 247px; height: 133px;
    background: var(--brand-green);
  }
  .benefit {
    position: absolute; top: 24px; width: 130px; margin-left: -65px;
    text-align: center; color: var(--white);
  }
  .benefit svg { display: block; margin: 0 auto; width: 70px; height: 70px; }
  .benefit-label {
    margin-top: 12px; font-size: 12px; font-weight: 700;
    letter-spacing: -0.2px; text-transform: uppercase;
  }

  .band-address {
    position: absolute; left: 0; right: 0; top: 252px; bottom: 0;
    background: var(--brand-green); color: var(--white);
    font-family: "Open Sans", sans-serif; font-weight: 600;
    font-size: 33px; text-align: center; line-height: 124px;
  }
</style>
</head>
<body>

<svg width="0" height="0" style="position:absolute" aria-hidden="true">
  <defs>
    <symbol id="icon-quiet" viewBox="0 0 70 70">
      <circle cx="35" cy="35" r="32" fill="none" stroke="#fff" stroke-width="3"/>
      <path d="M20 29h7l9-8v28l-9-8h-7z" fill="#fff"/>
      <path d="M42 29l10 12M52 29L42 41" stroke="#fff" stroke-width="3" stroke-linecap="round"/>
    </symbol>
    <symbol id="icon-clear-road" viewBox="0 0 70 70">
      <circle cx="35" cy="35" r="32" fill="none" stroke="#fff" stroke-width="3"/>
      <path d="M27 18L21 52M43 18l6 34" stroke="#fff" stroke-width="3" stroke-linecap="round"/>
      <path d="M35 20v6M35 32v6M35 44v6" stroke="#fff" stroke-width="3" stroke-linecap="round"/>
    </symbol>
    <symbol id="icon-speed" viewBox="0 0 70 70">
      <circle cx="35" cy="35" r="32" fill="none" stroke="#fff" stroke-width="3"/>
      <circle cx="35" cy="37" r="16" fill="none" stroke="#fff" stroke-width="3"/>
      <path d="M35 37l7-7M31 17h8" stroke="#fff" stroke-width="3" stroke-linecap="round"/>
    </symbol>
    <symbol id="icon-leaf" viewBox="0 0 70 70">
      <circle cx="35" cy="35" r="32" fill="none" stroke="#fff" stroke-width="3"/>
      <path d="M22 48C22 30 34 20 50 20C50 38 40 48 22 48z" fill="#fff"/>
      <path d="M22 48L40 30" stroke="#0e8c39" stroke-width="2.5" stroke-linecap="round"/>
    </symbol>
    <symbol id="icon-tick" viewBox="0 0 70 70">
      <circle cx="35" cy="35" r="32" fill="none" stroke="#fff" stroke-width="3"/>
      <path d="M22 36l9 9 17-19" fill="none" stroke="#fff" stroke-width="5" stroke-linecap="round" stroke-linejoin="round"/>
    </symbol>
  </defs>
</svg>

<div class="size-label" style="left:32px; top:198px;">54X30</div>
<div class="size-label" style="left:32px; top:600px;">54X30</div>
<div class="size-label" style="left:184px; top:967px;">37X33</div>

<section class="panel panel--wide" style="top:10px;">
  <div class="band-headline">
    <h1 class="headline headline--tight">STUCK IN TRAFFIC ?&nbsp; NOT ANYMORE</h1>
    <p class="subline subline--small">CHOOSE US...! THE BEST CARGO TRIKE SERVICE</p>
  </div>
  <div class="band-brand">
    <div class="brand-lockup">
      <div class="brand-name">HAULWAY</div>
      <div class="brand-dot"></div>
    </div>
    <div class="web-address">haulway-go.com</div>
  </div>
  <div class="band-benefits">
    <div class="benefit" style="left:100px;"><svg><use href="#icon-quiet"/></svg><div class="benefit-label">No noise</div></div>
    <div class="benefit" style="left:232px;"><svg><use href="#icon-clear-road"/></svg><div class="benefit-label">No traffic jam</div></div>
    <div class="benefit" style="left:370px;"><svg><use href="#icon-speed"/></svg><div class="benefit-label">Fast delivery</div></div>
    <div class="benefit" style="left:506px;"><svg><use href="#icon-leaf"/></svg><div class="benefit-label">Eco friendly</div></div>
    <div class="benefit" style="left:638px;"><svg><use href="#icon-tick"/></svg><div class="benefit-label">Advertising</div></div>
  </div>
</section>

<section class="panel panel--wide" style="top:414px;">
  <div class="band-headline">
    <h1 class="headline headline--spaced">ANYTHING TO ANYWHERE</h1>
    <p class="subline subline--large">THE BEST CARGO TRIKE SERVICE</p>
  </div>
  <div class="band-brand">
    <div class="brand-lockup">
      <div class="brand-name">HAULWAY</div>
      <div class="brand-dot"></div>
    </div>
    <div class="web-address">haulway-go.com</div>
  </div>
  <div class="band-benefits">
    <div class="benefit" style="left:100px;"><svg><use href="#icon-quiet"/></svg><div class="benefit-label">No noise</div></div>
    <div class="benefit" style="left:232px;"><svg><use href="#icon-clear-road"/></svg><div class="benefit-label">No traffic jam</div></div>
    <div class="benefit" style="left:370px;"><svg><use href="#icon-speed"/></svg><div class="benefit-label">Fast delivery</div></div>
    <div class="benefit" style="left:506px;"><svg><use href="#icon-leaf"/></svg><div class="benefit-label">Eco friendly</div></div>
    <div class="benefit" style="left:638px;"><svg><use href="#icon-tick"/></svg><div class="benefit-label">Advertising</div></div>
  </div>
</section>

<section class="panel panel--square">
  <div class="band-headline">
    <h1 class="headline headline--stacked">CONVEY YOUR IDEAS TO<br>THE WORLD</h1>
    <p class="subline subline--square">ADVERTISE WITH US</p>
  </div>
  <div class="band-brand">
    <div class="brand-lockup">
      <div class="brand-name">HAULWAY</div>
      <div class="brand-dot"></div>
    </div>
  </div>
  <div class="band-address">haulway-go.com</div>
</section>

</body>
</html>
```